corvena motor oil

I would like to inform you that our new motor oil brand corvena will be divided into three categories:
Corvena high performance Full Synthetic
0w20 ,5w30 ,0w16,5w20
with massage.
Maximum Protection, Ultimate Performance.corvena pellura
--------------------------------
corvena pellura Synthetic Blend
10w40,5w30,5w20
with massage
The perfect combination of durability and efficiency
-------------------------------
corvena olvendra transmission fluid
ATF III
with massage
proven to maximize transmission life

```html
<!DOCTYPE html>
<html lang="en">
<head>
<meta charset="utf-8">
<title>Corvena Motor Oil – Label Range</title>
<link href="https://fonts.googleapis.com/css2?family=Montserrat:ital,wght@0,400;0,500;0,600;0,700;0,800;1,400;1,500;1,600;1,700;1,800;1,900&display=swap" rel="stylesheet">
<style>
  :root{
    --canvas:#e4e4e6;
    --white:#f2f2f2;
    --red:#d8262c;
    --red-deep:#5c1417;
    --red-dark:#190b0c;
    --blue:#2f8fc4;
    --blue-deep:#17304a;
    --blue-dark:#0b121c;
    --purple:#9350d0;
    --purple-deep:#4a2a72;
    --purple-dark:#1c1428;
  }
  *{margin:0;padding:0;box-sizing:border-box}
  html,body{width:1200px;height:686px;overflow:hidden;background:var(--canvas)}
  body{position:relative;font-family:"Montserrat",sans-serif;color:var(--white)}

  .label{
    position:absolute;width:360px;height:468px;overflow:hidden;
    clip-path:polygon(0 76px,100% 0,100% 100%,0 100%);
    transform-origin:top left;
  }
  .label--pellura{left:70px;top:118px;--accent:var(--red);--deep:var(--red-deep);--dark:var(--red-dark)}
  .label--performance{left:470px;top:118px;--accent:var(--blue);--deep:var(--blue-deep);--dark:var(--blue-dark)}
  .label--olvendra{left:880px;top:224px;height:504px;transform:scale(0.7);
    clip-path:polygon(0 110px,100% 0,100% 100%,0 100%);
    --accent:var(--purple);--deep:var(--purple-deep);--dark:var(--purple-dark)}

  .label__ground{position:absolute;inset:0;
    background:linear-gradient(165deg,var(--deep) 0%,var(--dark) 62%,#0a0a0c 100%)}
  .label__graphics{position:absolute;inset:0;width:100%;height:100%}

  .brand-mark{position:absolute;top:124px;left:52px;display:flex;align-items:center;gap:10px}
  .brand-mark__dot{width:22px;height:22px;border:3px solid var(--white);border-radius:50%}
  .brand-mark__name{font-weight:800;font-size:24px;letter-spacing:2px;text-transform:uppercase;color:var(--white)}

  .line{position:absolute;left:28px;white-space:nowrap;line-height:1}
  .brand{top:198px;font-size:30px;font-weight:800;font-style:italic;letter-spacing:.5px}
  .product{font-weight:900;font-style:italic;color:var(--accent);letter-spacing:-.5px}
  .label--pellura .product{top:236px;left:22px;font-size:54px}
  .label--performance .product{font-size:36px;left:24px}
  .product--first{top:226px}
  .product--second{top:260px}
  .sub{font-weight:700;font-size:22px;letter-spacing:.8px}
  .label--pellura .sub{top:290px}
  .label--performance .sub{top:300px;font-size:21px}

  .grades{position:absolute;left:26px;display:flex;list-style:none;border:1.5px solid var(--accent)}
  .label--pellura .grades{top:326px}
  .label--performance .grades{top:334px}
  .grades__item{font-size:13px;font-weight:600;color:var(--accent);padding:6px 10px;letter-spacing:.5px}
  .label--performance .grades__item{font-size:12.5px;padding:6px 8px}
  .grades__item + .grades__item{border-left:1.5px solid var(--accent)}

  .rule{position:absolute;left:24px;width:232px;height:1.5px;background:var(--accent)}
  .label--pellura .rule{top:366px}
  .label--performance .rule{top:372px}

  .tagline{position:absolute;left:26px;font-size:13.5px;font-style:italic;font-weight:500;line-height:16px;letter-spacing:.3px;text-transform:uppercase}
  .label--pellura .tagline{top:380px}
  .label--performance .tagline{top:386px}
  .tagline__accent{color:var(--accent);font-weight:700}

  .foot{position:absolute;left:26px;top:434px;font-size:9.5px;font-weight:500;letter-spacing:.4px}
  .volume{position:absolute;left:280px;top:414px;text-align:center;line-height:1}
  .volume__amount{font-size:19px;font-weight:800;color:var(--accent)}
  .volume__word{font-size:7px;font-weight:500;margin-top:1px}

  /* transmission fluid label */
  .label--olvendra .brand-mark{top:168px}
  .label--olvendra .brand{top:236px}
  .label--olvendra .product{top:274px;font-size:46px}
  .label--olvendra .sub{top:326px;font-size:20px}
  .spec{position:absolute;left:28px;top:356px;padding:4px 10px 4px 8px;font-size:20px;font-weight:800;font-style:italic;
    color:var(--white);background:linear-gradient(90deg,var(--accent),rgba(147,80,208,0))}
  .label--olvendra .rule{top:396px;width:290px}
  .label--olvendra .tagline{top:410px;font-size:14px}
  .label--olvendra .foot{top:470px;font-size:10px}
  .label--olvendra .volume{top:450px}
</style>
</head>
<body>

  <!-- Pellura: synthetic blend -->
  <section class="label label--pellura">
    <div class="label__ground" role="img" aria-label="Dark red gradient with a subtle hexagon texture"></div>
    <svg class="label__graphics" viewBox="0 0 360 468" aria-hidden="true">
      <defs>
        <linearGradient id="redBand" x1="0" y1="0" x2="1" y2="0">
          <stop offset="0" stop-color="#d8262c" stop-opacity=".35"/>
          <stop offset="1" stop-color="#d8262c"/>
        </linearGradient>
      </defs>
      <polygon points="300,0 338,0 222,182 184,182" fill="#c1242a" opacity=".9"/>
      <polygon points="346,0 360,0 360,14 256,182 238,182" fill="#b21f25" opacity=".85"/>
      <line x1="360" y1="70" x2="252" y2="236" stroke="#8e1c20" stroke-width="1.5"/>
      <polygon points="240,324 360,324 360,346 262,346" fill="url(#redBand)"/>
      <polygon points="272,356 360,356 360,380 296,380" fill="url(#redBand)"/>
      <polygon points="304,390 360,390 360,412 326,412" fill="url(#redBand)"/>
    </svg>
    <div class="brand-mark"><span class="brand-mark__dot"></span><span class="brand-mark__name">Corvena</span></div>
    <p class="line brand">CORVENA</p>
    <h2 class="line product">PELLURA</h2>
    <p class="line sub">SYNTHETIC BLEND</p>
    <ul class="grades">
      <li class="grades__item">10W40</li>
      <li class="grades__item">5W20</li>
      <li class="grades__item">5W30</li>
    </ul>
    <div class="rule"></div>
    <p class="tagline">The perfect combination<br>of <span class="tagline__accent">durability and efficiency</span></p>
    <p class="foot">SYNTHETIC BLEND MOTOR OIL</p>
    <div class="volume"><div class="volume__amount">4L</div><div class="volume__word">Volume</div></div>
  </section>

  <!-- High performance: full synthetic -->
  <section class="label label--performance">
    <div class="label__ground" role="img" aria-label="Dark navy gradient with a subtle hexagon texture"></div>
    <svg class="label__graphics" viewBox="0 0 360 468" aria-hidden="true">
      <defs>
        <linearGradient id="blueBand" x1="0" y1="0" x2="1" y2="0">
          <stop offset="0" stop-color="#2f8fc4" stop-opacity=".35"/>
          <stop offset="1" stop-color="#2f8fc4"/>
        </linearGradient>
      </defs>
      <polygon points="300,0 338,0 222,182 184,182" fill="#2a7fb0" opacity=".9"/>
      <polygon points="346,0 360,0 360,14 256,182 238,182" fill="#236e9a" opacity=".85"/>
      <line x1="360" y1="70" x2="252" y2="236" stroke="#1e5578" stroke-width="1.5"/>
      <polygon points="262,330 360,330 360,352 284,352" fill="url(#blueBand)"/>
      <polygon points="288,362 360,362 360,386 310,386" fill="url(#blueBand)"/>
      <polygon points="312,396 360,396 360,418 332,418" fill="url(#blueBand)"/>
    </svg>
    <div class="brand-mark"><span class="brand-mark__dot"></span><span class="brand-mark__name">Corvena</span></div>
    <p class="line brand">CORVENA</p>
    <h2 class="line product product--first">HIGH</h2>
    <h2 class="line product product--second">PERFORMANCE</h2>
    <p class="line sub">FULL SYNTHETIC</p>
    <ul class="grades">
      <li class="grades__item">0W20</li>
      <li class="grades__item">5W30</li>
      <li class="grades__item">0W16</li>
      <li class="grades__item">5W20</li>
    </ul>
    <div class="rule"></div>
    <p class="tagline">Maximum protection,<br><span class="tagline__accent">ultimate performance</span></p>
    <p class="foot">SYNTHETIC BLEND MOTOR OIL</p>
    <div class="volume"><div class="volume__amount">4L</div><div class="volume__word">Volume</div></div>
  </section>

  <!-- Olvendra: transmission fluid -->
  <section class="label label--olvendra">
    <div class="label__ground" role="img" aria-label="Deep purple gradient with a subtle hexagon texture"></div>
    <svg class="label__graphics" viewBox="0 0 360 504" aria-hidden="true">
      <defs>
        <linearGradient id="purpleBand" x1="0" y1="0" x2="1" y2="0">
          <stop offset="0" stop-color="#9350d0" stop-opacity=".35"/>
          <stop offset="1" stop-color="#9350d0"/>
        </linearGradient>
      </defs>
      <polygon points="296,0 336,0 218,200 178,200" fill="#8a48c6" opacity=".9"/>
      <polygon points="346,0 360,0 360,16 252,200 234,200" fill="#7a3db2" opacity=".85"/>
      <line x1="360" y1="80" x2="246" y2="264" stroke="#5e2f8a" stroke-width="1.5"/>
      <polygon points="236,356 360,356 360,378 258,378" fill="url(#purpleBand)"/>
      <polygon points="270,388 360,388 360,412 294,412" fill="url(#purpleBand)"/>
      <polygon points="304,422 360,422 360,444 326,444" fill="url(#purpleBand)"/>
    </svg>
    <div class="brand-mark"><span class="brand-mark__dot"></span><span class="brand-mark__name">Corvena</span></div>
    <p class="line brand">CORVENA</p>
    <h2 class="line product">OLVENDRA</h2>
    <p class="line sub">TRANSMISSION FLUID</p>
    <p class="spec">ATF III</p>
    <div class="rule"></div>
    <p class="tagline">Proven to maximize<br><span class="tagline__accent">transmission life</span></p>
    <p class="foot">SYNTHETIC BLEND MOTOR OIL</p>
    <div class="volume"><div class="volume__amount">4L</div><div class="volume__word">Volume</div></div>
  </section>

</body>
</html>
```